Retail Appliance Store Chain needs NEW business Card

Name of my company is Brandon's Appliances brandonsappliances.com is our website. . We are a 2 location brick and mortar, and online store selling premium, luxury, and normal household appliances, such as ovens, stoves, cooktops, dishwashers, refrigerators, washers and dryers, grills, air conditioners etc. The focus is on large kitchen appliances and laundry appliances.
Please visit http://brandonsappliances.com to get a feel for the business and branding.
I have attached the Brandon's Appliances logo (i do not have eps or psd or ai). And I have also attached our current business cards that we use. We have two versions. A double sided version for managers, and a one side version for regular employees.
Please submit BOTH one sided and two sided designs if possible.
Please keep consistent with the Brandon's Appliances logo, colors, etc.
I would prefer no rounded corners on the business card designs for printing costs.
Information on the cards (in no particular order):
Name - Employee Name
Business name - Brandon's Appliances
website - brandonsappliances.com
Email - Employee Email
2 Phone Numbers - store 1 address, store 2 address
2 Addresses - store 1 address, store 2 address

*do NOT need Fax #

Industry/Entity Type

Home Appliance

Contact Information for Business Card

Logo - Brandons Appliances Logo
Name - Employee Name
Email - Employee Email

Please no rounded corners. Standard US Business Card Size please.

Font styles to use
Serif
Sans Serif

Requirements
Must have
• colors and design that somewhat match the feel of current logo and website
Should not have
• No rounded corners.
No non-traditional business card size. US Standard Business Card Size only

```html
<!DOCTYPE html>
<html lang="en">
<head>
<meta charset="utf-8">
<title>Brandon's Appliances – Business Cards</title>
<link href="https://fonts.googleapis.com/css2?family=Roboto:wght@400;500;700&display=swap" rel="stylesheet">
<style>
  :root {
    --backdrop: #d4d4d6;
    --card-white: #f4f4f6;
    --brand-blue: #0b4a98;
    --brand-blue-deep: #083a7a;
    --stripe-grey: #5a5a5c;
    --text-grey: #6b6b6e;
    --on-blue: #ffffff;
  }
  * { box-sizing: border-box; margin: 0; padding: 0; }
  html, body { width: 1200px; height: 800px; overflow: hidden; }
  body {
    background: var(--backdrop);
    font-family: "Roboto", Arial, sans-serif;
    position: relative;
  }
  .card {
    position: absolute;
    top: 246px;
    width: 540px;
    height: 309px;
    overflow: hidden;
    box-shadow: 0 6px 18px rgba(0,0,0,0.18);
  }
  .card-front { left: 40px; background: var(--card-white); }
  .card-back { left: 620px; background: var(--brand-blue); }

  .front-wave { position: absolute; inset: 0; width: 100%; height: 100%; }

  .brand-name {
    position: absolute;
    font-weight: 700;
    color: var(--brand-blue);
    white-space: nowrap;
  }
  .card-front .brand-name { left: 28px; top: 160px; font-size: 27px; }

  .employee {
    position: absolute;
    right: 150px;
    top: 20px;
    text-align: right;
    line-height: 1.3;
  }
  .employee-name { font-size: 19px; font-weight: 700; color: var(--brand-blue); letter-spacing: 0.3px; }
  .employee-role, .employee-email { font-size: 10.5px; color: var(--text-grey); }

  .locations {
    position: absolute;
    right: 20px;
    top: 98px;
    text-align: right;
    color: var(--on-blue);
    font-size: 10.5px;
    line-height: 1.4;
  }
  .location + .location { margin-top: 8px; }
  .location-name { font-weight: 700; font-size: 11.5px; }
  .contact-line { display: flex; justify-content: flex-end; align-items: center; gap: 5px; }
  .contact-line svg { width: 10px; height: 10px; fill: var(--on-blue); }

  .card-back .brand-name {
    left: 0; right: 0; top: 118px;
    text-align: center;
    font-size: 34px;
    color: var(--brand-blue-deep);
  }
  .back-url {
    position: absolute;
    left: 0; right: 0; top: 222px;
    text-align: center;
    color: var(--on-blue);
    font-size: 12px;
    letter-spacing: 3px;
  }
</style>
</head>
<body>

<section class="card card-front" aria-label="Business card front">
  <svg class="front-wave" viewBox="0 0 540 309" preserveAspectRatio="none" aria-hidden="true">
    <path d="M430 0 C400 90 360 170 285 220 C200 275 85 298 0 304 L0 309 L540 309 L540 0 Z" fill="var(--stripe-grey)"/>
    <path transform="translate(10 0)" d="M430 0 C400 90 360 170 285 220 C200 275 85 298 -10 305 L-10 309 L540 309 L540 0 Z" fill="var(--card-white)"/>
    <path transform="translate(14 0)" d="M430 0 C400 90 360 170 285 220 C200 275 85 300 -14 307 L-14 309 L540 309 L540 0 Z" fill="var(--brand-blue)"/>
  </svg>

  <div class="brand-name">Brandon's Appliances</div>

  <div class="employee">
    <div class="employee-name">MARCUS HALE</div>
    <div class="employee-role">Bargain Basement Supervisor, Lakeport</div>
    <div class="employee-email">marcush@brandonsappliances.com</div>
  </div>

  <div class="locations">
    <div class="location">
      <div class="location-name">Lakeport</div>
      <div>145 Harbor View Rd.</div>
      <div>Lakeport, CT 06101</div>
      <div class="contact-line">
        <svg viewBox="0 0 24 24" aria-hidden="true"><path d="M6.6 10.8a15 15 0 0 0 6.6 6.6l2.2-2.2a1 1 0 0 1 1-.25 11.4 11.4 0 0 0 3.6.57 1 1 0 0 1 1 1V20a1 1 0 0 1-1 1A17 17 0 0 1 3 4a1 1 0 0 1 1-1h3.5a1 1 0 0 1 1 1c0 1.25.2 2.45.57 3.6a1 1 0 0 1-.25 1z"/></svg>
        <span>(555) 210-4837</span>
      </div>
      <div class="contact-line">
        <svg viewBox="0 0 24 24" aria-hidden="true"><path d="M6 2h9v6H6zM3 9h18v11H3zm3 3v2h12v-2z"/></svg>
        <span>(555) 210-4890</span>
      </div>
    </div>
    <div class="location">
      <div class="location-name">Bayfield</div>
      <div>18 Willow Creek Ave.</div>
      <div>Bayfield, CT 06102</div>
      <div class="contact-line">
        <svg viewBox="0 0 24 24" aria-hidden="true"><path d="M6.6 10.8a15 15 0 0 0 6.6 6.6l2.2-2.2a1 1 0 0 1 1-.25 11.4 11.4 0 0 0 3.6.57 1 1 0 0 1 1 1V20a1 1 0 0 1-1 1A17 17 0 0 1 3 4a1 1 0 0 1 1-1h3.5a1 1 0 0 1 1 1c0 1.25.2 2.45.57 3.6a1 1 0 0 1-.25 1z"/></svg>
        <span>(555) 318-6624</span>
      </div>
      <div class="contact-line">
        <svg viewBox="0 0 24 24" aria-hidden="true"><path d="M6 2h9v6H6zM3 9h18v11H3zm3 3v2h12v-2z"/></svg>
        <span>(555) 210-4890</span>
      </div>
    </div>
  </div>
</section>

<section class="card card-back" aria-label="Business card back">
  <div class="brand-name">Brandon's Appliances</div>
  <div class="back-url">www.brandonsappliances.com</div>
</section>

</body>
</html>
```